Business Card Design - Local Discount Club

Looking for a fun business card for a local discount club. One side should be the logo only and the other should be have :

Name
Title
Phone, Email
Website

```html
<!DOCTYPE html>
<html lang="en">
<head>
<meta charset="utf-8">
<title>Harbor Lane Pass – Business Card</title>
<link rel="stylesheet" href="https://fonts.googleapis.com/css2?family=Montserrat:wght@700&family=Open+Sans:wght@400&display=swap">
<style>
  :root {
    --backdrop: #d6d5d3;
    --card-white: #ffffff;
    --brand-blue: #3f5aa9;
    --brand-navy: #2d3f98;
    --brand-sky: #5aa9dc;
    --text-grey: #5a5a5a;
    --rule: #3f5aa9;
  }
  * { margin: 0; padding: 0; box-sizing: border-box; }
  html, body { width: 1200px; height: 801px; overflow: hidden; }
  body {
    background: var(--backdrop);
    display: flex;
    align-items: center;
    justify-content: center;
    gap: 60px;
    font-family: "Open Sans", Arial, sans-serif;
  }
  .card {
    width: 500px;
    height: 286px;
    position: relative;
    box-shadow: 0 6px 18px rgba(0,0,0,0.18);
  }
  .card--front { background: var(--card-white); border-bottom: 3px solid var(--brand-blue); }
  .card--back {
    background: var(--brand-blue);
    display: flex;
    align-items: center;
    justify-content: center;
  }
  .brand-name {
    font-family: "Montserrat", Arial, sans-serif;
    font-weight: 700;
    color: var(--brand-navy);
    display: flex;
    align-items: center;
    gap: 10px;
    white-space: nowrap;
  }
  .brand-name__dot {
    width: 14px; height: 14px;
    border-radius: 50%;
    background: var(--brand-sky);
    flex: none;
  }
  .card--front .brand-name {
    position: absolute;
    top: 62px;
    left: 0; right: 0;
    justify-content: center;
    font-size: 30px;
    letter-spacing: 0.5px;
  }
  .card--back .brand-name {
    font-size: 40px;
    color: #2f4590;
    letter-spacing: 1px;
  }
  .card--back .brand-name__dot { width: 22px; height: 22px; background: #7fb0e0; }
  .details {
    position: absolute;
    left: 0; right: 0;
    top: 150px;
    display: flex;
    justify-content: center;
    align-items: stretch;
    gap: 18px;
  }
  .person { text-align: right; display: flex; flex-direction: column; justify-content: flex-end; padding-bottom: 2px; }
  .person__name {
    font-family: "Montserrat", Arial, sans-serif;
    font-weight: 700;
    font-size: 17px;
    color: var(--brand-navy);
    letter-spacing: 0.3px;
  }
  .person__title { font-size: 12px; color: var(--text-grey); margin-top: 2px; }
  .divider { width: 1px; background: var(--rule); }
  .contact { list-style: none; display: flex; flex-direction: column; gap: 5px; }
  .contact__item {
    display: flex; align-items: center; gap: 7px;
    font-size: 12.5px; color: var(--text-grey);
  }
  .contact__icon { width: 12px; height: 12px; flex: none; }
</style>
</head>
<body>
  <section class="card card--front" aria-label="Business card front">
    <div class="brand-name"><span class="brand-name__dot"></span>HARBOR LANE PASS</div>
    <div class="details">
      <div class="person">
        <p class="person__name">DANA WHITCOMBE</p>
        <p class="person__title">President</p>
      </div>
      <div class="divider"></div>
      <ul class="contact">
        <li class="contact__item">
          <svg class="contact__icon" viewBox="0 0 12 12"><circle cx="6" cy="6" r="6" fill="#3f5aa9"/><path d="M4 3.2l1 1.3-.6.7c.4.9 1 1.5 1.9 1.9l.7-.6 1.3 1-.5 1c-2.3-.2-4.3-2.2-4.5-4.5z" fill="#fff"/></svg>
          555-014-2290
        </li>
        <li class="contact__item">
          <svg class="contact__icon" viewBox="0 0 12 12"><rect x="0.5" y="2.5" width="11" height="7" rx="1" fill="#3f5aa9"/><path d="M1 3l5 3.5L11 3" stroke="#fff" stroke-width="1" fill="none"/></svg>
          hello@harborlanepass.com
        </li>
        <li class="contact__item">
          <svg class="contact__icon" viewBox="0 0 12 12"><circle cx="6" cy="6" r="5.5" fill="#3f5aa9"/><path d="M0.5 6h11M6 0.5c-2 2-2 9 0 11M6 0.5c2 2 2 9 0 11" stroke="#fff" stroke-width="0.8" fill="none"/></svg>
          www.harborlanepass.com
        </li>
      </ul>
    </div>
  </section>

  <section class="card card--back" aria-label="Business card back">
    <div class="brand-name"><span class="brand-name__dot"></span>HARBOR LANE PASS</div>
  </section>
</body>
</html>
```